Stylish Website Design for Harbour Crate Lagoons

Harbour Crate Lagoons will be building a new website in a Wordpress CMS.
The design will be stylish, clean with strong powerful images that represent their work. Users scrolling pages will have call to actions listed at various intervals that drives traffic through the website journey.
The objective of the website journey is to direct clients to the ‘Instant Quote’. This will take visitors through an 8 Step calculator.
1. Capture Customer Details (Email and Full Name).
2. Pool Size
3. Shell Colour
4. Exterior Colour
5. Decking Option
6. Access Options
7. Selections (choosing the sanitisation and pump)
8. Extras
The instant quote will be visually appealing and engaging. The next button for each step will capture the data and identify the step the customer aborts.
Here is a link to the current calculator OLD QUOTE: https://harbourcratelagoons.example.au/quote
The current design has the following issues that need to be resolved with the new design, please do not replicate the current look and feel. We are seeking a complete redesign of the website.
1. No scrolling to go to the next tap.
2. Improve the image layout
3. Selections and Extras needs to be like an eCommerce site with images, access to descriptions, specifications etc.
4. The steps need to feel like a journey
5. Gathering the customer’s name and email must be captured at the beginning
The aim is to keep the design simple but stylish. The navigation should have a search bar and clearly display the phone number as a link not an image, so it can be clicked on to make a call from a mobile device.
Please note the current website does not have the current logo, only a temporary one. Please use this one, the logo may be redesigned. https://filebay.example.net/external/a1f4c9d2e7b83056f1c2d4e9a7b6c3d8e5f1a2b7c9d0e4f6a8b3c5d7e9f0a1b2
IMAGES: Here are some of the company’s professional images. https://filebay.example.net/external/c7e2a9f1b4d6083e5a1c9f7b2d4e6a8c0f3b5d7e9a1c2f4b6d8e0a3c5f7b9d1e
There must be call to actions as you scroll the page.
• Contact Us Button
• Download Brochure (name may be changed)
o This will capture a customers name and email to send a brochure
• Join Our Team
• Live Chat (Floats bottom right)
• Order Now Button
Site Map
• Home page – via logo
• Design and Build - http://harbourcratelagoons.example.au/learn-more
o Instant Quote
o Packages
There may be 3 packages
o The Process
o Financing
• About Us
o Choosing Us
o Locations
o Careers
• Blogs
o Events
o Legends
• Gallery
• Contact Us
Footer
• Social Media icons
o TikTok
o Instagram
o Facebook
o Youtube
o Twitter
• Privacy Policy (Content on the current site but improve layout)
• Specifications
• Site Map
• Images of Certifications (as shown on the current site)
• Company Contact Details (Address on Phone)
• Marketing News Sign Up
Target Market(s)
Business to Consumer, Renovations
Industry/Entity Type
Construction and Renovations
Number of Pages Required
5+ page
Requirements
Must have
- Read the description but home page design and calculator design.
Nice to have
- Included in the description.

```html
<!DOCTYPE html>
<html lang="en">
<head>
<meta charset="utf-8">
<title>Harbour Crate Lagoons — Instant Quote Screens</title>
<link rel="stylesheet" href="https://fonts.googleapis.com/css2?family=Poppins:wght@300;400;500;600&display=swap">
<style>
:root{
  --stage:#0b5c60;
  --paper:#ffffff;
  --bar:#c9c5c6;
  --footer:#c3c9c9;
  --ink:#222222;
  --muted:#555555;
  --sky:#80c5dc;
  --sky-deep:#6fb6cf;
  --sky-line:#9fd3e3;
  --track:#b5acae;
  --chip:#c2c9c9;
  --card:#e4e4e4;
  --card-foot:#dadada;
  --orange:#f39a1e;
  --duck:#f7d21a;
}
*{box-sizing:border-box;margin:0;padding:0}
html,body{width:1200px;height:827px;overflow:hidden;background:var(--stage)}
body{font-family:"Poppins",sans-serif;color:var(--ink)}
.stage{position:absolute;left:0;top:0;width:2000px;height:1378px;transform:scale(.6);transform-origin:0 0;background:var(--stage)}
.screen{position:absolute;top:136px;width:516px;background:var(--paper);overflow:hidden}
.screen--details{left:152px;height:968px}
.screen--size{left:758px;height:1129px}
.screen--extras{left:1320px;height:1129px}

.callbar{height:26px;background:var(--bar);display:flex;align-items:center;justify-content:center;gap:10px;color:#fff;font-size:12px;font-weight:500;letter-spacing:3.2px}
.callbar a{color:inherit;text-decoration:none}
.callbar svg{width:20px;height:20px}

.brand{position:absolute;left:13px;top:46px;display:flex;align-items:center;gap:5px}
.brand__dot{width:14px;height:14px;border-radius:50%;background:var(--orange)}
.brand__name{color:var(--orange);font-size:11px;font-weight:400;line-height:1.15;width:60px}

.nav{position:absolute;top:38px;left:187px;font-size:9.5px;letter-spacing:2px;line-height:1.05;text-transform:uppercase}
.nav a{color:var(--ink);text-decoration:none;position:absolute;white-space:nowrap}
.nav a.is-current{color:var(--sky)}

.page-title{position:absolute;top:126px;left:0;width:100%;text-align:center;font-size:21px;font-weight:400;letter-spacing:5px}

.progress{position:absolute;left:0;top:184px;width:516px;height:30px}
.duck{position:absolute;top:188px;width:22px;height:22px;border-radius:50%;background:var(--duck)}

.step-heading{position:absolute;top:260px;font-size:15px;font-weight:400;letter-spacing:3.2px;text-transform:uppercase}
.step-heading b{color:var(--sky);font-weight:500;font-size:19px;letter-spacing:2px}

.lede{position:absolute;font-size:10px;font-weight:400;line-height:1.25;color:var(--ink);letter-spacing:.3px}

.field{position:absolute;left:26px;width:462px;height:45px;border:1.5px solid var(--sky-line);border-radius:6px;padding:0 18px;display:flex;align-items:center;font-size:13px;letter-spacing:2.2px;color:var(--muted)}

.pager{position:absolute;display:flex;gap:10px}
.pager svg{width:38px;height:38px}

.pool-photo{position:absolute;left:29px;top:347px;width:458px;height:192px;border-radius:14px;background:linear-gradient(160deg,#8fd2ea 0%,#5bb9dc 55%,#7cc8e4 100%)}
.pool-photo__dots{position:absolute;left:194px;bottom:11px;display:flex;gap:3px}
.pool-photo__dots i{display:block;width:17px;height:2px;background:#fff;opacity:.8}
.pool-photo__dots i:first-child{opacity:1}

.options-title{position:absolute;left:29px;top:596px;font-size:15px;font-weight:400;letter-spacing:3.4px;color:var(--sky);text-transform:uppercase}

.size-option{position:absolute;top:676px;width:198px;height:186px;border-radius:8px;color:#fff;text-align:center;overflow:hidden}
.size-option--active{left:29px;background:var(--sky);box-shadow:0 3px 0 var(--sky-line)}
.size-option--idle{left:288px;background:var(--chip)}
.size-option__dim{position:absolute;left:0;width:100%;font-size:34px;font-weight:600;letter-spacing:3px;line-height:1}
.size-option__dim span{font-weight:300;font-size:28px;letter-spacing:0}
.size-option__by{position:absolute;left:0;width:100%;top:76px;font-size:22px;font-weight:300}
.size-option__tag{position:absolute;left:164px;top:154px;font-size:12px;letter-spacing:1.5px;color:#e9eded}

.extra{position:absolute;width:143px;height:199px;border-radius:8px;background:var(--card)}
.extra--chosen{background:var(--sky);color:#fff}
.extra__photo{position:absolute;left:20px;top:-42px;width:120px;height:84px;border-radius:10px;background:radial-gradient(circle at 45% 55%,#3d4346 0%,#25292b 55%,#7d8589 100%)}
.extra__name{position:absolute;left:16px;top:48px;width:120px;font-size:11px;font-weight:500;letter-spacing:1.3px;line-height:1.2;text-transform:uppercase}
.extra__text{position:absolute;left:14px;top:86px;width:110px;font-size:6.8px;line-height:1.2;text-align:justify;color:#555}
.extra--chosen .extra__text{color:#eef7fa}
.extra__price{position:absolute;right:20px;top:141px;font-size:13px;font-weight:500;letter-spacing:1.5px}
.extra__action{position:absolute;left:0;bottom:0;width:100%;height:30px;border-top:2px solid #fff;border-radius:0 0 8px 8px;background:var(--card-foot);display:flex;align-items:center;justify-content:center;font-size:13px;letter-spacing:1.6px;text-transform:uppercase}
.extra--chosen .extra__action{background:var(--sky-deep)}

.footer{position:absolute;left:0;bottom:0;width:516px;height:137px;background:var(--footer);font-size:9px;letter-spacing:.4px}
.footer__link{position:absolute;line-height:1.15;color:var(--ink);text-decoration:none}
.footer__brand{position:absolute;right:14px;top:22px;display:flex;align-items:center;gap:4px}
.footer__brand i{width:9px;height:9px;border-radius:50%;background:var(--ink)}
.footer__brand span{font-size:7px;line-height:1.1;width:44px}
.footer__note{position:absolute;right:16px;top:72px;text-align:right;line-height:1.1}
.footer__rule{position:absolute;left:8px;right:8px;top:102px;height:2px;background:#eef0f0}
.footer__legal{position:absolute;left:26px;top:118px;display:flex;gap:11px;font-size:7px}
.footer__social{position:absolute;right:15px;top:108px;display:flex;gap:6px}
.footer__social i{width:20px;height:20px;border-radius:50%;background:#111}
</style>
</head>
<body>
<div class="stage">

  <!-- Step 1 -->
  <section class="screen screen--details">
    <div class="callbar"><svg viewBox="0 0 20 20"><circle cx="10" cy="10" r="10" fill="#8f8789"/><path d="M6.5 5.2l2 .1.8 2.3-1.2.9c.6 1.4 1.6 2.4 3 3l.9-1.2 2.3.8.1 2c-.1.7-.7 1.2-1.4 1.2C9.3 14.2 5.8 10.7 5.5 6.6c0-.7.4-1.3 1-1.4z" fill="#fff"/></svg><a href="tel:1234567890">CALL US NOW : 1234567890</a></div>
    <div class="brand"><i class="brand__dot"></i><span class="brand__name">Harbour Crate Lagoons</span></div>
    <nav class="nav"><a class="is-current" style="left:0">Instant<br>Quote</a><a style="left:71px">Financial<br>Calculator</a><a style="left:170px">Gallery</a><a style="left:248px">Contact</a></nav>
    <h1 class="page-title">INSTANT QUOTE</h1>
    <svg class="progress" viewBox="0 0 516 30"><line x1="27" y1="15" x2="489" y2="15" stroke="#b5acae" stroke-width="3"/><g fill="#b0a8aa"><circle cx="93" cy="15" r="6"/><circle cx="161" cy="15" r="6"/><circle cx="228" cy="15" r="6"/><circle cx="294" cy="15" r="6"/><circle cx="359" cy="15" r="6"/><circle cx="424" cy="15" r="6"/><circle cx="489" cy="15" r="6"/></g></svg>
    <span class="duck" style="left:16px" role="img" aria-label="Rubber duck progress marker"></span>
    <h2 class="step-heading" style="left:32px"><b>1.</b>Help us with your details</h2>
    <p class="lede" style="left:33px;top:308px;width:455px">Lorem ipsum dolor sit amet, consectetur adipiscing elit, Lorem ipsum dolor sit amet, consectetur adipiscing elit,</p>
    <div class="field" style="top:363px">Name</div>
    <div class="field" style="top:437px">Mail address</div>
    <div class="field" style="top:510px">Phone Number</div>
    <div class="field" style="top:581px">Post Code</div>
    <div class="field" style="top:652px">How do you hear about us?</div>
    <div class="pager" style="left:401px;top:742px">
      <svg viewBox="0 0 38 38"><circle cx="19" cy="19" r="19" fill="#cbcbcb"/><polyline points="22,12 15,19 22,26" fill="none" stroke="#fff" stroke-width="3.5" stroke-linecap="round" stroke-linejoin="round"/></svg>
      <svg viewBox="0 0 38 38"><circle cx="19" cy="19" r="19" fill="#6cc0dc"/><polyline points="16,12 23,19 16,26" fill="none" stroke="#fff" stroke-width="3.5" stroke-linecap="round" stroke-linejoin="round"/></svg>
    </div>
    <footer class="footer">
      <a class="footer__link" style="left:26px;top:23px">Home</a><a class="footer__link" style="left:133px;top:23px">Why Us</a><a class="footer__link" style="left:241px;top:23px">Careers</a>
      <a class="footer__link" style="left:26px;top:49px">Instant<br>Quote</a><a class="footer__link" style="left:133px;top:49px">Financial<br>Calculator</a><a class="footer__link" style="left:241px;top:49px">Help</a>
      <a class="footer__link" style="left:26px;top:83px">About Us</a><a class="footer__link" style="left:133px;top:83px">Contact</a><a class="footer__link" style="left:241px;top:83px">Brochure</a>
      <div class="footer__brand"><i></i><span>Harbour Crate Lagoons</span></div>
      <p class="footer__note">Lorem ipsum<br>dolor sit amet,</p>
      <div class="footer__rule"></div>
      <div class="footer__legal"><span>Site Map</span><span>Privacy POlicy</span><span>Cookies</span></div>
      <div class="footer__social"><i></i><i></i><i></i><i></i></div>
    </footer>
  </section>

  <!-- Step 2 -->
  <section class="screen screen--size">
    <div class="callbar"><svg viewBox="0 0 20 20"><circle cx="10" cy="10" r="10" fill="#8f8789"/><path d="M6.5 5.2l2 .1.8 2.3-1.2.9c.6 1.4 1.6 2.4 3 3l.9-1.2 2.3.8.1 2c-.1.7-.7 1.2-1.4 1.2C9.3 14.2 5.8 10.7 5.5 6.6c0-.7.4-1.3 1-1.4z" fill="#fff"/></svg><a href="tel:1234567890">CALL US NOW : 1234567890</a></div>
    <div class="brand"><i class="brand__dot"></i><span class="brand__name">Harbour Crate Lagoons</span></div>
    <nav class="nav"><a class="is-current" style="left:0">Instant<br>Quote</a><a style="left:71px">Financial<br>Calculator</a><a style="left:170px">Gallery</a><a style="left:248px">Contact</a></nav>
    <h1 class="page-title">INSTANT QUOTE</h1>
    <svg class="progress" viewBox="0 0 516 30"><line x1="28" y1="15" x2="488" y2="15" stroke="#b5acae" stroke-width="3"/><line x1="28" y1="15" x2="94" y2="15" stroke="#80c5dc" stroke-width="3"/><circle cx="28" cy="15" r="6" fill="#fff" stroke="#80c5dc" stroke-width="2"/><polyline points="25,15 27.5,17.5 31.5,12.5" fill="none" stroke="#80c5dc" stroke-width="1.6"/><g fill="#b0a8aa"><circle cx="161" cy="15" r="6"/><circle cx="227" cy="15" r="6"/><circle cx="293" cy="15" r="6"/><circle cx="358" cy="15" r="6"/><circle cx="424" cy="15" r="6"/><circle cx="488" cy="15" r="6"/></g></svg>
    <span class="duck" style="left:83px" role="img" aria-label="Rubber duck progress marker"></span>
    <h2 class="step-heading" style="left:32px"><b>2.</b>Pool size</h2>
    <div class="pool-photo" role="img" aria-label="Photo of a container pool in perspective beside its top view, set on rippling pool water"><div class="pool-photo__dots"><i></i><i></i><i></i></div></div>
    <h3 class="options-title">Two options available</h3>
    <p class="lede" style="left:29px;top:632px">Lorem ipsum dolor sit amet, consectetur adipiscing elit,</p>
    <div class="size-option size-option--active"><div class="size-option__dim" style="top:36px">6 <span>m</span></div><div class="size-option__by">x</div><div class="size-option__dim" style="top:108px">2.4 <span>m</span></div></div>
    <div class="size-option size-option--idle"><div class="size-option__dim" style="top:36px">12 <span>m</span></div><div class="size-option__by">x</div><div class="size-option__dim" style="top:108px">2.4 <span>m</span></div><span class="size-option__tag">REMOVE</span></div>
    <div class="pager" style="left:400px;top:900px">
      <svg viewBox="0 0 38 38"><circle cx="19" cy="19" r="19" fill="#6cc0dc"/><polyline points="22,12 15,19 22,26" fill="none" stroke="#fff" stroke-width="3.5" stroke-linecap="round" stroke-linejoin="round"/></svg>
      <svg viewBox="0 0 38 38"><circle cx="19" cy="19" r="19" fill="#6cc0dc"/><polyline points="16,12 23,19 16,26" fill="none" stroke="#fff" stroke-width="3.5" stroke-linecap="round" stroke-linejoin="round"/></svg>
    </div>
    <footer class="footer">
      <a class="footer__link" style="left:13px;top:23px">Home</a><a class="footer__link" style="left:120px;top:23px">Why Us</a><a class="footer__link" style="left:227px;top:23px">Careers</a>
      <a class="footer__link" style="left:13px;top:49px">Instant<br>Quote</a><a class="footer__link" style="left:120px;top:49px">Financial<br>Calculator</a><a class="footer__link" style="left:227px;top:49px">Help</a>
      <a class="footer__link" style="left:13px;top:83px">About Us</a><a class="footer__link" style="left:120px;top:83px">Contact</a><a class="footer__link" style="left:227px;top:83px">Brochure</a>
      <div class="footer__brand"><i></i><span>Harbour Crate Lagoons</span></div>
      <p class="footer__note" style="right:28px">Lorem ipsum<br>dolor sit amet,</p>
      <div class="footer__rule"></div>
      <div class="footer__legal" style="left:13px"><span>Site Map</span><span>Privacy POlicy</span><span>Cookies</span></div>
      <div class="footer__social" style="right:27px"><i></i><i></i><i></i><i></i></div>
    </footer>
  </section>

  <!-- Step 7 -->
  <section class="screen screen--extras">
    <div class="callbar"><svg viewBox="0 0 20 20"><circle cx="10" cy="10" r="10" fill="#8f8789"/><path d="M6.5 5.2l2 .1.8 2.3-1.2.9c.6 1.4 1.6 2.4 3 3l.9-1.2 2.3.8.1 2c-.1.7-.7 1.2-1.4 1.2C9.3 14.2 5.8 10.7 5.5 6.6c0-.7.4-1.3 1-1.4z" fill="#fff"/></svg><a href="tel:1234567890">CALL US NOW : 1234567890</a></div>
    <div class="brand"><i class="brand__dot"></i><span class="brand__name">Harbour Crate Lagoons</span></div>
    <nav class="nav"><a class="is-current" style="left:0">Instant<br>Quote</a><a style="left:71px">Financial<br>Calculator</a><a style="left:170px">Gallery</a><a style="left:248px">Contact</a></nav>
    <h1 class="page-title">INSTANT QUOTE</h1>
    <svg class="progress" viewBox="0 0 516 30"><line x1="28" y1="15" x2="488" y2="15" stroke="#b5acae" stroke-width="3"/><line x1="28" y1="15" x2="423" y2="15" stroke="#80c5dc" stroke-width="3"/><g fill="#fff" stroke="#80c5dc" stroke-width="2"><circle cx="28" cy="15" r="6"/><circle cx="93" cy="15" r="6"/><circle cx="161" cy="15" r="6"/><circle cx="227" cy="15" r="6"/><circle cx="293" cy="15" r="6"/><circle cx="358" cy="15" r="6"/></g><g fill="none" stroke="#80c5dc" stroke-width="1.6"><polyline points="25,15 27.5,17.5 31.5,12.5"/><polyline points="90,15 92.5,17.5 96.5,12.5"/><polyline points="158,15 160.5,17.5 164.5,12.5"/><polyline points="224,15 226.5,17.5 230.5,12.5"/><polyline points="290,15 292.5,17.5 296.5,12.5"/><polyline points="355,15 357.5,17.5 361.5,12.5"/></g><circle cx="488" cy="15" r="6" fill="#b0a8aa"/></svg>
    <span class="duck" style="left:412px" role="img" aria-label="Rubber duck progress marker"></span>
    <h2 class="step-heading" style="left:32px"><b>7.</b>Extras</h2>

    <article class="extra extra--chosen" style="left:17px;top:381px"><div class="extra__photo" role="img" aria-label="Product photo of a swim jet pump"></div><h4 class="extra__name">Tidewell<br>Swim Jet</h4><p class="extra__text">Lorem ipsum dolor sit amet, consectetur adipiscing elit, sed do eiusmod tempor incididunt ut labore et dolore magna aliqua. Quis</p><span class="extra__price">$ 3435</span><span class="extra__action">Remove</span></article>
    <article class="extra" style="left:185px;top:381px"><div class="extra__photo" role="img" aria-label="Product photo of a heater pump"></div><h4 class="extra__name" style="top:55px">Heater Pump</h4><p class="extra__text">Lorem ipsum dolor sit amet, consectetur adipiscing elit, sed do eiusmod tempor incididunt ut labore et dolore magna aliqua. Quis</p><span class="extra__price">$ 3435</span><span class="extra__action">Add</span></article>
    <article class="extra" style="left:353px;top:381px"><div class="extra__photo" role="img" aria-label="Product photo of a sand filter"></div><h4 class="extra__name" style="top:55px">Sand Filter</h4><p class="extra__text">Lorem ipsum dolor sit amet, consectetur adipiscing elit, sed do eiusmod tempor incididunt ut labore et dolore magna aliqua. Quis</p><span class="extra__price">$ 3435</span><span class="extra__action">Add</span></article>

    <article class="extra" style="left:16px;top:655px"><div class="extra__photo" role="img" aria-label="Product photo of a heater pump"></div><h4 class="extra__name" style="top:48px">Heater Pump</h4><p class="extra__text">Lorem ipsum dolor sit amet, consectetur adipiscing elit, sed do eiusmod tempor incididunt ut labore et dolore magna aliqua. Quis</p><span class="extra__price">$ 3435</span><span class="extra__action">Add</span></article>
    <article class="extra" style="left:185px;top:653px"><div class="extra__photo" role="img" aria-label="Product photo of a heater pump"></div><h4 class="extra__name" style="top:48px">Heater Pump</h4><p class="extra__text">Lorem ipsum dolor sit amet, consectetur adipiscing elit, sed do eiusmod tempor incididunt ut labore et dolore magna aliqua. Quis</p><span class="extra__price">$ 3435</span><span class="extra__action">Add</span></article>
    <article class="extra extra--chosen" style="left:355px;top:653px"><div class="extra__photo" role="img" aria-label="Product photo of a swim jet pump"></div><h4 class="extra__name">Tidewell<br>Swim Jet</h4><p class="extra__text">Lorem ipsum dolor sit amet, consectetur adipiscing elit, sed do eiusmod tempor incididunt ut labore et dolore magna aliqua. Quis</p><span class="extra__price">$ 3435</span><span class="extra__action">Remove</span></article>

    <div class="pager" style="left:400px;top:900px">
      <svg viewBox="0 0 38 38"><circle cx="19" cy="19" r="19" fill="#6cc0dc"/><polyline points="22,12 15,19 22,26" fill="none" stroke="#fff" stroke-width="3.5" stroke-linecap="round" stroke-linejoin="round"/></svg>
      <svg viewBox="0 0 38 38"><circle cx="19" cy="19" r="19" fill="#6cc0dc"/><polyline points="16,12 23,19 16,26" fill="none" stroke="#fff" stroke-width="3.5" stroke-linecap="round" stroke-linejoin="round"/></svg>
    </div>
    <footer class="footer">
      <a class="footer__link" style="left:13px;top:23px">Home</a><a class="footer__link" style="left:120px;top:23px">Why Us</a><a class="footer__link" style="left:227px;top:23px">Careers</a>
      <a class="footer__link" style="left:13px;top:49px">Instant<br>Quote</a><a class="footer__link" style="left:120px;top:49px">Financial<br>Calculator</a><a class="footer__link" style="left:227px;top:49px">Help</a>
      <a class="footer__link" style="left:13px;top:83px">About Us</a><a class="footer__link" style="left:120px;top:83px">Contact</a><a class="footer__link" style="left:227px;top:83px">Brochure</a>
      <div class="footer__brand"><i></i><span>Harbour Crate Lagoons</span></div>
      <p class="footer__note" style="right:28px">Lorem ipsum<br>dolor sit amet,</p>
      <div class="footer__rule"></div>
      <div class="footer__legal" style="left:13px"><span>Site Map</span><span>Privacy POlicy</span><span>Cookies</span></div>
      <div class="footer__social" style="right:27px"><i></i><i></i><i></i><i></i></div>
    </footer>
  </section>

</div>
</body>
</html>
```